PowerPoint Strategy presentation to be converted to professional looking

Convert the supplied PowerPoint presentation to a professional strategy presentation. Designer must have knowledge of how strategies are presented.

Target Market(s)

Management team

Industry/Entity Type

Finance

Font styles to use
Sans Serif

Colors
0054AA
0677BA
7BADD7
CADEEF
E8F1F8

Requirements
Must have
• Strategy must look professional
Nice to have
• Animations would be welcomed

```html
<!DOCTYPE html>
<html lang="en">
<head>
<meta charset="utf-8">
<title>SHF Transformation 2026 – ExCom Alignment Deck</title>
<link href="https://fonts.googleapis.com/css2?family=Open+Sans:wght@400;600;700;800&display=swap" rel="stylesheet">
<style>
:root{
  --blue:#0054AA;
  --blue-mid:#0677BA;
  --blue-light:#7BADD7;
  --blue-pale:#CADEEF;
  --blue-wash:#E8F1F8;
  --blue-deep:#003B7A;
  --ink:#1f2a37;
  --text:#3a4656;
  --grey:#8a96a3;
  --line:#d5e2ee;
  --paper:#ffffff;
}
*{box-sizing:border-box;margin:0;padding:0}
html,body{width:1200px;height:1200px;overflow:hidden;background:var(--paper)}
body{font-family:"Open Sans",sans-serif;color:var(--ink);position:relative}
.slide{position:absolute;width:260px;height:146px;background:linear-gradient(160deg,var(--blue-wash) 0%,#ffffff 42%,#f6f9fc 100%);box-shadow:0 2px 6px rgba(0,40,90,.18);overflow:hidden}
.title{position:absolute;left:20px;top:9px;font-size:7.6px;font-weight:700;color:var(--blue);white-space:nowrap}
.brand{position:absolute;right:8px;top:9px;display:flex;align-items:center;gap:2px;font-size:3.6px;font-weight:700;color:var(--blue)}
.brand i{display:block;width:4px;height:4px;border-radius:50%;background:var(--blue)}
.foot{position:absolute;left:14px;right:12px;bottom:5px;border-top:.4px solid var(--blue-light);padding-top:1px;display:flex;justify-content:space-between;font-size:2.6px;color:var(--blue-mid)}
.foot.center{justify-content:center}
.foot.plain{border:0}
svg{position:absolute;left:0;top:0}
.fb{fill:var(--blue)} .fm{fill:var(--blue-mid)} .fl{fill:var(--blue-light)} .fp{fill:var(--blue-pale)} .fd{fill:var(--blue-deep)} .fw{fill:#fff} .fg{fill:#9aa6b2}
.sb{stroke:var(--blue)} .sm{stroke:var(--blue-mid)} .sl{stroke:var(--blue-light)} .sd{stroke:var(--blue-deep)}
.kh{position:absolute;font-size:3.4px;line-height:1.4;color:var(--text)}
.kh b.h{display:block;color:var(--blue);font-size:5px;font-weight:700;margin-bottom:2px}
.kh ul{padding-left:4px}
.kh li{margin-bottom:1.4px}
.kh b{color:var(--ink)}
/* cover */
.cover-frame{position:absolute;left:18px;top:29px;width:224px;height:89px;border:1.4px solid var(--blue);background:#fff}
.cover-block{position:absolute;top:0;bottom:0;width:73px;background:linear-gradient(135deg,var(--blue-mid),var(--blue));color:#fff;display:flex;flex-direction:column;justify-content:center;align-items:center;text-align:center}
.cover-block b{font-size:9.5px;line-height:1.1;font-weight:700}
.cover-block span{font-size:5px;line-height:1.2;margin-top:2px}
.cover-name{position:absolute;font-size:6.5px;font-weight:700;color:var(--blue)}
.cover-tag{position:absolute;font-size:3px;color:var(--grey)}
.cover-main{position:absolute;font-size:12.5px;font-weight:800;color:var(--ink);text-align:center;line-height:1.05}
.cover-main small{display:block;font-size:8.6px}
/* agenda */
.agenda-block{position:absolute;left:13px;top:17px;width:95px;height:108px;background:linear-gradient(135deg,var(--blue-mid),var(--blue));color:#fff;font-size:11px;font-weight:700;display:flex;align-items:center;justify-content:center}
.agenda-list{position:absolute;left:120px;top:50px;font-size:7.2px;line-height:1.65;list-style:none;color:var(--ink)}
.agenda-list span{color:var(--blue-mid)}
/* section */
.section-line{position:absolute;left:50px;right:50px;height:.6px;background:var(--blue)}
.section-line.grey{background:var(--grey)}
.section-dot{position:absolute;width:26px;height:26px;border-radius:50%;background:var(--blue)}
.section-text{position:absolute;left:0;right:0;text-align:center;font-size:9.2px;font-weight:700;color:var(--text)}
/* statement */
.statement-head{position:absolute;left:27px;top:20px;font-size:13px;line-height:1.05;font-weight:700;color:var(--blue)}
.statement-body{position:absolute;left:27px;top:66px;width:120px;font-size:3.5px;line-height:1.7;color:var(--text)}
.statement-art{position:absolute;left:170px;top:20px;width:80px;height:116px;background:linear-gradient(180deg,var(--blue-wash),var(--blue-pale))}
.statement-door{position:absolute;left:186px;top:44px;width:46px;height:80px;background:linear-gradient(180deg,var(--blue-mid),var(--blue))}
/* pills */
.pill{position:absolute;height:15px;border-radius:8px;font-size:4.4px;font-weight:700;display:flex;align-items:center;line-height:1.15}
.pill.now{background:var(--blue-pale);color:var(--blue-deep);width:90px;left:24px;padding-left:18px}
.pill.next{background:var(--blue);color:#fff;width:90px;left:125px;padding-left:8px}
.col-label{position:absolute;font-size:4.6px;font-weight:700}
/* KPI */
.kpi-head{position:absolute;top:34px;height:10px;color:#fff;font-size:4.2px;font-weight:700;display:flex;align-items:center;justify-content:center}
.kpi-row{position:absolute;display:flex;align-items:center;font-size:4.6px;height:10px;color:var(--ink)}
.chev{height:10px;color:#fff;font-size:3.4px;font-weight:700;display:flex;align-items:center;justify-content:center;text-align:center;line-height:1;clip-path:polygon(0 0,88% 0,100% 50%,88% 100%,0 100%,12% 50%)}
.kpi-row .v{width:24px;text-align:center}
/* pillars */
.pillar{position:absolute;top:52px;width:41px;height:62px;color:#fff;font-size:4.3px;font-weight:700;text-align:center;display:flex;flex-direction:column;justify-content:flex-end;padding-bottom:13px;line-height:1.15}
.card{position:absolute;background:#fff;border:.5px solid var(--line);border-radius:3px;box-shadow:0 1px 2px rgba(0,40,90,.12);overflow:hidden}
.card-head{background:var(--blue);color:#fff;font-size:3.6px;font-weight:700;text-align:center;padding:2px 1px;line-height:1.15}
.card-body{font-size:3px;line-height:1.45;color:var(--text);padding:3px 3px}
.card-body li{list-style:none;padding-left:3px;text-indent:-3px;margin-bottom:2px}
.card-body li::before{content:"• ";color:var(--blue-mid)}
.bar{position:absolute;background:var(--blue-deep);color:#fff;font-size:4.2px;font-weight:700;text-align:center;height:8px;line-height:8px}
.tile{position:absolute;background:linear-gradient(180deg,var(--blue-mid),var(--blue));color:#fff;font-size:3.8px;font-weight:700;text-align:center;display:flex;align-items:center;justify-content:center;line-height:1.2;border-radius:1px}
.tile-note{position:absolute;font-size:2.9px;line-height:1.35;color:var(--text);text-align:center}
.badge{position:absolute;right:6px;top:5px;width:33px;height:33px;border-radius:50%;background:var(--blue);color:#fff;text-align:center;font-size:2.6px;line-height:1.1;padding-top:6px}
.badge b{display:block;font-size:8px}
.sub{position:absolute;left:0;right:0;text-align:center;font-size:4.2px;color:var(--text)}
</style>
</head>
<body>

<!-- Row 1 -->
<section class="slide" style="left:51px;top:106px">
  <div class="cover-frame">
    <div class="cover-block" style="left:0"><b>ExCom<br>Alignment</b><span>Transformation<br>Strategy</span></div>
    <div class="cover-name" style="left:110px;top:12px">Sanad Home Finance</div>
    <div class="cover-tag" style="left:104px;top:24px">Specialists in Home Financing Solutions</div>
    <div class="cover-main" style="left:78px;right:4px;top:56px">SHF Transformation<small>2026</small></div>
  </div>
  <div class="foot center plain"><span>© Copyright 2023 Sanad Home Finance. All Rights Reserved.</span></div>
</section>

<section class="slide" style="left:331px;top:106px">
  <div class="cover-frame">
    <div class="cover-name" style="left:40px;top:12px">Sanad Home Finance</div>
    <div class="cover-tag" style="left:33px;top:24px">Specialists in Home Financing Solutions</div>
    <div class="cover-main" style="left:2px;width:146px;top:56px">SHF Transformation<small>2026</small></div>
    <div style="position:absolute;right:8px;top:16px;width:62px;text-align:center;color:var(--blue);line-height:1.05">
      <b style="font-size:9.5px">ExCom<br>Alignment</b><div style="font-size:5px;margin-top:2px;color:var(--blue-mid)">Transformation<br>Strategy</div></div>
  </div>
  <div class="foot center plain"><span>© Copyright 2023 Sanad Home Finance. All Rights Reserved.</span></div>
</section>

<section class="slide" style="left:611px;top:106px;background:linear-gradient(120deg,#fff,var(--blue-wash))">
  <div class="brand"><i></i>Sanad Home Finance</div>
  <div class="agenda-block">AGENDA</div>
  <ol class="agenda-list">
    <li><span>1.</span> Current State Evaluation</li>
    <li><span>2.</span> Strategy and Financial Plan</li>
    <li><span>3.</span> Other Initiatives</li>
  </ol>
  <div class="foot"><span>3</span><span>© Copyright 2023 Sanad Home Finance. All Rights Reserved.</span></div>
</section>

<section class="slide" style="left:890px;top:106px">
  <div class="brand"><i></i>Sanad Home Finance</div>
  <div class="section-line" style="top:43px"></div>
  <div class="section-dot" style="left:113px;top:30px"></div>
  <div class="section-text" style="top:64px">1. Current State Evaluation</div>
  <div class="section-line grey" style="top:95px;left:65px;right:50px"></div>
  <div class="foot center plain"><span>© Copyright 2023 Sanad Home Finance. All Rights Reserved.</span></div>
</section>

<!-- Row 2 -->
<section class="slide" style="left:51px;top:316px">
  <div class="title">SHF vs. Market Production and Forecast</div>
  <div class="brand"><i></i>Sanad Home Finance</div>
  <svg width="260" height="146" viewBox="0 0 260 146">
    <text x="44" y="31" font-size="3.2" font-weight="700" fill="#1f2a37">SHF vs. Market Historical Production</text>
    <text x="136" y="31" font-size="3.2" font-weight="700" fill="#1f2a37">Forecast</text>
    <g stroke="#dfe8f1" stroke-width=".3">
      <line x1="34" y1="37" x2="172" y2="37"/><line x1="34" y1="52" x2="172" y2="52"/><line x1="34" y1="67" x2="172" y2="67"/><line x1="34" y1="82" x2="172" y2="82"/><line x1="34" y1="97" x2="172" y2="97"/><line x1="34" y1="112" x2="172" y2="112"/>
    </g>
    <rect x="118" y="33" width="49" height="81" fill="none" class="sb" stroke-width=".6"/>
    <g font-size="2.8" fill="#3a4656">
      <text x="19" y="38">250,000</text><text x="19" y="53">200,000</text><text x="19" y="68">150,000</text><text x="19" y="83">100,000</text><text x="22" y="98">50,000</text><text x="30" y="113">0</text>
      <text x="38" y="118">2019</text><text x="54" y="118">2020</text><text x="70" y="118">2021</text><text x="86" y="118">2022</text><text x="102" y="118">2023</text><text x="118" y="118">2024</text><text x="134" y="118">2025</text><text x="150" y="118">2026</text>
    </g>
    <polyline points="43,46 59,42 75,58 91,73 107,85 123,77 139,69 155,61" fill="none" class="sd" stroke-width=".8"/>
    <polyline points="43,72 59,82 75,88 91,91 107,91 123,82 139,74 155,67" fill="none" class="sl" stroke-width=".8"/>
    <g class="fd">
      <rect x="37" y="40" width="12" height="3.6"/><rect x="53" y="37" width="12" height="3.6"/>
      <rect x="69" y="53" width="12" height="3.6"/><rect x="85" y="68" width="12" height="3.6"/>
      <rect x="101" y="80" width="12" height="3.6"/><rect x="117" y="72" width="12" height="3.6"/>
      <rect x="133" y="64" width="12" height="3.6"/><rect x="149" y="56" width="12" height="3.6"/>
    </g>
    <g class="fm">
      <rect x="37" y="74" width="12" height="3.6"/><rect x="53" y="84" width="10" height="3.6"/>
      <rect x="69" y="90" width="10" height="3.6"/><rect x="85" y="93" width="10" height="3.6"/>
      <rect x="101" y="93" width="12" height="3.6"/><rect x="117" y="84" width="12" height="3.6"/>
      <rect x="133" y="76" width="12" height="3.6"/><rect x="149" y="69" width="12" height="3.6"/>
    </g>
    <g font-size="2.3" fill="#fff">
      <text x="38" y="42.8">225,073</text><text x="54" y="39.8">232,500</text><text x="70" y="55.8">201,481</text><text x="86" y="70.8">154,392</text><text x="102" y="82.8">120,000</text><text x="118" y="74.8">130,000</text><text x="134" y="66.8">140,000</text><text x="150" y="58.8">150,000</text>
      <text x="39" y="76.8">3,075</text><text x="54" y="86.8">2,381</text><text x="70" y="92.8">1,769</text><text x="86" y="95.8">1,395</text><text x="103" y="95.8">1,696</text><text x="119" y="86.8">2,406</text><text x="135" y="78.8">2,771</text><text x="151" y="71.8">3,107</text>
    </g>
    <rect x="36" y="121" width="21" height="4" fill="none" stroke="#9aa6b2" stroke-width=".3"/>
    <text x="37.5" y="123.9" font-size="2.3" fill="#3a4656">SHF Market Share</text>
    <line x1="80" y1="123" x2="86" y2="123" class="sm" stroke-width=".8"/><text x="87" y="124" font-size="2.8" fill="#3a4656">SHF</text>
    <line x1="98" y1="123" x2="104" y2="123" class="sd" stroke-width=".8"/><text x="105" y="124" font-size="2.8" fill="#3a4656">Market</text>
  </svg>
  <div class="kh" style="left:180px;top:28px;width:73px">
    <b class="h">Key Highlights</b>
    <b>Historical</b>
    <ul><li>Overall mortgage output keeps easing for the fourth year in a row, to about 100,000 units</li><li>SHF is set to grow sales by about a fifth in 2023, against a market fall</li></ul>
    <b>Forecast</b>
    <ul><li>Market output is forecast to reach 150,000 units by 2026, led by off plan and self construction</li><li>SHF is forecast to grow output by over 80% in the next three years</li></ul>
  </div>
  <div class="foot"><span>5</span><span>© Copyright 2023 Sanad Home Finance. All Rights Reserved.</span></div>
</section>

<section class="slide" style="left:331px;top:316px">
  <div class="title">Market Production Mix – HSF Share</div>
  <div class="brand"><i></i>Sanad Home Finance</div>
  <svg width="260" height="146" viewBox="0 0 260 146">
    <text x="74" y="31" font-size="3.2" font-weight="700" fill="#3a4656">HSF vs. Non HSF Share</text>
    <g stroke="#dfe8f1" stroke-width=".3">
      <line x1="22" y1="36" x2="180" y2="36"/><line x1="22" y1="52" x2="180" y2="52"/><line x1="22" y1="68" x2="180" y2="68"/><line x1="22" y1="84" x2="180" y2="84"/><line x1="22" y1="100" x2="180" y2="100"/><line x1="22" y1="116" x2="180" y2="116"/>
    </g>
    <g font-size="2.8" fill="#3a4656"><text x="14" y="37">90%</text><text x="14" y="53">70%</text><text x="14" y="69">50%</text><text x="14" y="85">30%</text><text x="14" y="101">10%</text>
      <text x="36" y="121">2019</text><text x="67" y="121">2020</text><text x="98" y="121">2021</text><text x="129" y="121">2022</text><text x="160" y="121">2023</text></g>
    <polyline points="41,48 72,54 103,58 134,61 165,63" fill="none" class="sd" stroke-width=".8"/>
    <polyline points="41,95 72,88 103,84 134,81 165,78" fill="none" class="sl" stroke-width=".8"/>
    <g class="fd"><rect x="36" y="44.5" width="10" height="3.6"/><rect x="67" y="50.5" width="10" height="3.6"/><rect x="98" y="54.5" width="10" height="3.6"/><rect x="129" y="57.5" width="10" height="3.6"/><rect x="160" y="59.5" width="10" height="3.6"/></g>
    <g class="fm"><rect x="36" y="91.5" width="10" height="3.6"/><rect x="67" y="84.5" width="10" height="3.6"/><rect x="98" y="80.5" width="10" height="3.6"/><rect x="129" y="77.5" width="10" height="3.6"/><rect x="160" y="74.5" width="10" height="3.6"/></g>
    <g font-size="2.5" fill="#fff"><text x="38" y="47.3">79%</text><text x="69" y="53.3">73%</text><text x="100" y="57.3">69%</text><text x="131" y="60.3">67%</text><text x="162" y="62.3">64%</text>
      <text x="38" y="94.3">21%</text><text x="69" y="87.3">27%</text><text x="100" y="83.3">31%</text><text x="131" y="80.3">33%</text><text x="162" y="77.3">36%</text></g>
    <line x1="74" y1="126" x2="80" y2="126" class="sm" stroke-width=".8"/><text x="81" y="127" font-size="2.8" fill="#3a4656">HSF</text>
    <line x1="92" y1="126" x2="98" y2="126" class="sd" stroke-width=".8"/><text x="99" y="127" font-size="2.8" fill="#3a4656">Non HSF</text>
  </svg>
  <div class="kh" style="left:188px;top:42px;width:64px"><b class="h">Key Highlights</b><ul><li>Non HSF share has grown over the last four years and now makes up 36% of total mortgage output</li><li>The shift is driven by a steady fall in HSF subsidy sales since 2019</li><li>Banks are leading the growth in non subsidy lending</li></ul></div>
  <div class="foot"><span>6</span><span>© Copyright 2023 Sanad Home Finance. All Rights Reserved.</span></div>
</section>

<section class="slide" style="left:611px;top:316px">
  <div class="title">Market Production Mix – HSF Products</div>
  <div class="brand"><i></i>Sanad Home Finance</div>
  <svg width="260" height="146" viewBox="0 0 260 146">
    <text x="72" y="31" font-size="3.2" font-weight="700" fill="#3a4656">HSF Product Breakdown</text>
    <g stroke="#dfe8f1" stroke-width=".3">
      <line x1="24" y1="36" x2="182" y2="36"/><line x1="24" y1="54" x2="182" y2="54"/><line x1="24" y1="72" x2="182" y2="72"/><line x1="24" y1="90" x2="182" y2="90"/><line x1="24" y1="108" x2="182" y2="108"/>
    </g>
    <g font-size="2.8" fill="#3a4656"><text x="16" y="37">80%</text><text x="16" y="55">60%</text><text x="16" y="73">40%</text><text x="16" y="91">20%</text><text x="17" y="109">0%</text>
      <text x="38" y="115">2019</text><text x="69" y="115">2020</text><text x="100" y="115">2021</text><text x="131" y="115">2022</text><text x="162" y="115">2023</text></g>
    <polyline points="43,48 74,71 105,66 136,56 167,46" fill="none" class="sd" stroke-width=".8"/>
    <polyline points="43,78 74,73 105,76 136,82 167,92" fill="none" class="sm" stroke-width=".8"/>
    <polyline points="43,99 74,97 105,96 136,97 167,97" fill="none" class="sl" stroke-width=".8"/>
    <g class="fd"><rect x="38" y="44.5" width="10" height="3.6"/><rect x="69" y="67.5" width="10" height="3.6"/><rect x="100" y="62.5" width="10" height="3.6"/><rect x="131" y="52.5" width="10" height="3.6"/><rect x="162" y="42.5" width="10" height="3.6"/></g>
    <g class="fm"><rect x="38" y="74.5" width="10" height="3.6"/><rect x="69" y="69.5" width="10" height="3.6"/><rect x="100" y="72.5" width="10" height="3.6"/><rect x="131" y="78.5" width="10" height="3.6"/><rect x="162" y="88.5" width="10" height="3.6"/></g>
    <g class="fl"><rect x="38" y="95.5" width="10" height="3.6"/><rect x="69" y="93.5" width="10" height="3.6"/><rect x="100" y="92.5" width="10" height="3.6"/><rect x="131" y="93.5" width="10" height="3.6"/><rect x="162" y="97.5" width="10" height="3.6"/></g>
    <g font-size="2.5" fill="#fff"><text x="40" y="47.3">63%</text><text x="71" y="70.3">48%</text><text x="102" y="65.3">50%</text><text x="133" y="55.3">60%</text><text x="164" y="45.3">69%</text>
      <text x="40" y="77.3">30%</text><text x="71" y="72.3">42%</text><text x="102" y="75.3">38%</text><text x="133" y="81.3">29%</text><text x="164" y="91.3">18%</text></g>
    <g font-size="2.5" fill="#003B7A"><text x="41" y="98.3">7%</text><text x="71" y="96.3">10%</text><text x="102" y="95.3">12%</text><text x="133" y="96.3">11%</text><text x="164" y="100.3">13%</text></g>
    <line x1="48" y1="125" x2="54" y2="125" class="sd" stroke-width=".8"/><text x="55" y="126" font-size="2.8" fill="#3a4656">Ready Unit</text>
    <line x1="80" y1="125" x2="86" y2="125" class="sm" stroke-width=".8"/><text x="87" y="126" font-size="2.8" fill="#3a4656">Off Plan</text>
    <line x1="108" y1="125" x2="114" y2="125" class="sl" stroke-width=".8"/><text x="115" y="126" font-size="2.8" fill="#3a4656">Self Construction</text>
  </svg>
  <div class="kh" style="left:188px;top:32px;width:64px"><b class="h">Key Highlights</b><ul><li>Self Construction fell in 2022 due to changes in ministry rules</li><li>Off Plan and Self Construction now make up over 30% of HSF subsidy output</li><li>Off Plan will keep growing in line with new ministry and national developer project plans</li></ul></div>
  <div class="foot"><span>7</span><span>© Copyright 2023 Sanad Home Finance. All Rights Reserved.</span></div>
</section>

<section class="slide" style="left:890px;top:316px">
  <div class="title">SHF vs. Market Production Mix</div>
  <div class="brand"><i></i>Sanad Home Finance</div>
  <svg width="260" height="146" viewBox="0 0 260 146">
    <rect x="24" y="24" width="56" height="6" class="fb"/><text x="39" y="28.4" font-size="3.6" font-weight="700" fill="#fff">SHF (2023)</text>
    <rect x="82" y="24" width="56" height="6" class="fg"/><text x="87" y="28.4" font-size="3.6" font-weight="700" fill="#fff">HSF Market (2023)</text>
    <rect x="140" y="24" width="44" height="6" class="fm"/><text x="145" y="28.4" font-size="3.4" font-weight="700" fill="#fff">SHF Opportunity</text>
    <rect x="14" y="34" width="8" height="30" class="fb"/><rect x="14" y="67" width="8" height="30" class="fb"/><rect x="14" y="100" width="8" height="28" class="fb"/>
    <g font-size="3.4" fill="#fff"><text transform="translate(19.5,60) rotate(-90)">Product</text><text transform="translate(19.5,92) rotate(-90)">Region</text><text transform="translate(19.5,120) rotate(-90)">HSF</text></g>
    <circle cx="40" cy="49" r="10" class="fb"/><path d="M40 49 L40 39 A10 10 0 0 1 45 40.3Z" class="fd"/>
    <circle cx="40" cy="82" r="10" class="fb"/><path d="M40 82 L40 72 A10 10 0 0 1 50 82Z" class="fd"/><path d="M40 82 L50 82 A10 10 0 0 1 42 92Z" class="fl"/>
    <circle cx="40" cy="114" r="10" class="fb"/><path d="M40 114 L40 104 A10 10 0 0 1 49 110Z" class="fl"/>
    <circle cx="98" cy="49" r="10" class="fb"/><path d="M98 49 L98 39 A10 10 0 0 0 89 44Z" class="fd"/><path d="M98 49 L89 44 A10 10 0 0 0 88 50Z" class="fl"/>
    <circle cx="98" cy="82" r="10" class="fb"/><path d="M98 82 L98 72 A10 10 0 0 0 88 82Z" class="fd"/><path d="M98 82 L88 82 A10 10 0 0 0 93 91Z" class="fl"/>
    <circle cx="98" cy="114" r="10" class="fb"/><path d="M98 114 L98 104 A10 10 0 0 0 89 118Z" class="fl"/>
    <g font-size="2.5" fill="#3a4656"><text x="53" y="44">Ready Unit</text><text x="53" y="49">Off Plan</text><text x="53" y="54">Self-Constr.</text>
      <text x="53" y="77">Makkah</text><text x="53" y="82">Riyadh</text><text x="53" y="87">Eastern</text><text x="53" y="111">HSF</text><text x="53" y="116">Non HSF</text>
      <text x="111" y="44">Ready Unit</text><text x="111" y="49">Off Plan</text><text x="111" y="54">Self-Constr.</text>
      <text x="111" y="77">Makkah</text><text x="111" y="82">Riyadh</text><text x="111" y="87">Eastern</text><text x="111" y="92">Non-Main</text><text x="111" y="114">HSF</text>
      <text x="142" y="44">Off Plan: 450M</text><text x="142" y="50">Self Constr.: 150M</text>
      <text x="142" y="77" font-weight="700">Ready Unit</text><text x="142" y="82">Riyadh: 450M</text><text x="142" y="87">Non-Main: 200M</text></g>
    <g class="fd"><rect x="50" y="41.8" width="2" height="2"/><rect x="50" y="74.8" width="2" height="2"/><rect x="50" y="108.8" width="2" height="2"/><rect x="108" y="41.8" width="2" height="2"/><rect x="108" y="74.8" width="2" height="2"/><rect x="108" y="111.8" width="2" height="2"/></g>
    <g class="fb"><rect x="50" y="46.8" width="2" height="2"/><rect x="50" y="79.8" width="2" height="2"/><rect x="50" y="113.8" width="2" height="2"/><rect x="108" y="46.8" width="2" height="2"/><rect x="108" y="79.8" width="2" height="2"/></g>
    <g class="fl"><rect x="50" y="51.8" width="2" height="2"/><rect x="50" y="84.8" width="2" height="2"/><rect x="108" y="51.8" width="2" height="2"/><rect x="108" y="84.8" width="2" height="2"/><rect x="108" y="89.8" width="2" height="2"/></g>
  </svg>
  <div class="kh" style="left:188px;top:24px;width:66px;font-size:3.1px"><b class="h">Key Highlights</b><ul><li><b>Product:</b> HSF non ready unit output makes up 32% of the addressable market</li><li><b>Region:</b> Riyadh is 10% below market average. Non main regions make up just 9% of SHF output vs. 35% for the market</li><li><b>HSF:</b> SHF holds a higher share of HSF output as bookings grew faster than market</li></ul></div>
  <div class="foot"><span>8</span><span>© Copyright 2023 Sanad Home Finance. All Rights Reserved.</span></div>
</section>

<!-- Row 3 -->
<section class="slide" style="left:51px;top:526px">
  <div class="title">SHF Production Mix</div>
  <div class="brand"><i></i>Sanad Home Finance</div>
  <svg width="260" height="146" viewBox="0 0 260 146">
    <rect x="32" y="25" width="108" height="6" class="fb"/><text x="74" y="29.4" font-size="3.6" font-weight="700" fill="#fff">SHF (2023)</text>
    <rect x="18" y="35" width="9" height="28" class="fb"/><rect x="18" y="66" width="9" height="28" class="fb"/><rect x="18" y="97" width="9" height="28" class="fb"/>
    <g font-size="3.4" fill="#fff"><text transform="translate(24,58) rotate(-90)">Income</text><text transform="translate(24,92) rotate(-90)">Property</text><text transform="translate(24,122) rotate(-90)">Loan Size</text></g>
    <circle cx="66" cy="48" r="10" class="fb"/><path d="M66 48 L66 38 A10 10 0 0 1 74 43Z" class="fd"/><path d="M66 48 L66 38 A10 10 0 0 0 57 43Z" class="fl"/>
    <circle cx="66" cy="80" r="10" class="fb"/><path d="M66 80 L66 70 A10 10 0 0 1 71 71.5Z" class="fd"/>
    <circle cx="66" cy="111" r="10" class="fb"/><path d="M66 111 L66 101 A10 10 0 0 1 73 104Z" class="fd"/><path d="M66 111 L66 101 A10 10 0 0 0 58 105Z" class="fl"/>
    <g font-size="2.8" fill="#3a4656"><text x="84" y="42">Up to 10K</text><text x="84" y="46.5">10K – 15K</text><text x="84" y="51">15K – 20K</text><text x="84" y="55.5">20K+</text>
      <text x="84" y="76">Villa</text><text x="84" y="80.5">Apartment</text><text x="84" y="85">Land</text>
      <text x="84" y="105">Up to 750K</text><text x="84" y="109.5">750K – 1M</text><text x="84" y="114">1M – 1.5M</text><text x="84" y="118.5">1.5M+</text></g>
    <g><rect x="80" y="39.8" width="2.4" height="2.4" class="fb"/><rect x="80" y="44.3" width="2.4" height="2.4" class="fl"/><rect x="80" y="48.8" width="2.4" height="2.4" class="fd"/><rect x="80" y="53.3" width="2.4" height="2.4" class="fp"/>
      <rect x="80" y="73.8" width="2.4" height="2.4" class="fb"/><rect x="80" y="78.3" width="2.4" height="2.4" class="fd"/><rect x="80" y="82.8" width="2.4" height="2.4" class="fl"/>
      <rect x="80" y="102.8" width="2.4" height="2.4" class="fb"/><rect x="80" y="107.3" width="2.4" height="2.4" class="fd"/><rect x="80" y="111.8" width="2.4" height="2.4" class="fl"/><rect x="80" y="116.3" width="2.4" height="2.4" class="fp"/></g>
  </svg>
  <div class="kh" style="left:148px;top:38px;width:100px;font-size:3.4px"><b class="h">Key Highlights</b><ul><li><b>Income and Property Type:</b> Changes to the HSF subsidy table have driven output towards buyers with income below 10K and apartment units with lower loan amounts</li><li><b>Loan Amount:</b> SHF is focused below SAR 750K. We have a plan to add new features and loan products to raise the average loan size.</li></ul></div>
  <div class="foot"><span>9</span><span>© Copyright 2023 Sanad Home Finance. All Rights Reserved.</span></div>
</section>

<section class="slide" style="left:331px;top:526px">
  <div class="title">SHF and NBFI Market Share</div>
  <div class="brand"><i></i>Sanad Home Finance</div>
  <svg width="260" height="146" viewBox="0 0 260 146">
    <text x="24" y="34" font-size="3.4" font-weight="700" fill="#1f2a37">2023 YTD NBFI share of overall</text><text x="44" y="38.5" font-size="3.4" font-weight="700" fill="#1f2a37">production</text>
    <circle cx="52" cy="78" r="28" class="fb"/><path d="M52 78 L52 50 A28 28 0 0 1 59 51Z" class="fd"/>
    <text x="40" y="92" font-size="2.8" fill="#fff">96% – SAR 72B</text><text x="28" y="48" font-size="2.8" fill="#3a4656">4% – SAR 3B</text>
    <g font-size="2.8" fill="#3a4656"><text x="86" y="74">Non-NBFI HSF</text><text x="86" y="80">NBFI HSF Share</text></g>
    <rect x="82.6" y="71.8" width="2.4" height="2.4" class="fb"/><rect x="82.6" y="77.8" width="2.4" height="2.4" class="fd"/>
    <text x="128" y="32" font-size="3.2" font-weight="700" fill="#1f2a37">2023 YTD SHF share of total NBFI</text><text x="148" y="36" font-size="3.2" font-weight="700" fill="#1f2a37">production</text>
    <circle cx="152" cy="54" r="14" class="fl"/><path d="M152 54 L152 40 A14 14 0 0 1 154 68Z" class="fb"/>
    <g font-size="2.6" fill="#3a4656"><text x="117" y="56">53% – SAR 1.4B</text><text x="168" y="44">47% – SAR 1.2B</text><text x="172" y="54">SHF NBFI Share</text><text x="172" y="59">NBFI HSF Share</text></g>
    <rect x="168.8" y="51.8" width="2.4" height="2.4" class="fb"/><rect x="168.8" y="56.8" width="2.4" height="2.4" class="fl"/>
    <text x="132" y="80" font-size="3.2" font-weight="700" fill="#1f2a37">2023 YTD SHF share of overall</text><text x="148" y="84" font-size="3.2" font-weight="700" fill="#1f2a37">production</text>
    <circle cx="152" cy="108" r="16" class="fb"/><path d="M152 108 L152 92 A16 16 0 0 0 150.6 92.1Z" class="fd"/>
    <g font-size="2.6" fill="#3a4656"><text x="124" y="94">1.4% – SAR 1.2B</text><text x="172" y="104">Bank and NBFI Share</text><text x="172" y="109">SHF Market Share</text></g>
    <text x="140" y="118" font-size="2.6" fill="#fff">98.6% – SAR 79B</text>
    <rect x="168.8" y="101.8" width="2.4" height="2.4" class="fb"/><rect x="168.8" y="106.8" width="2.4" height="2.4" class="fd"/>
  </svg>
  <div class="foot"><span>10</span><span>© Copyright 2023 Sanad Home Finance. All Rights Reserved.</span></div>
</section>

<section class="slide" style="left:611px;top:526px">
  <div class="title">SHF SWOT Analysis</div>
  <div class="brand"><i></i>Sanad Home Finance</div>
  <svg width="260" height="146" viewBox="0 0 260 146">
    <line x1="130" y1="26" x2="130" y2="128" stroke="#c7d6e5" stroke-width=".4"/><line x1="16" y1="78" x2="246" y2="78" stroke="#c7d6e5" stroke-width=".4"/>
    <path d="M130 79 L130 50 A29 29 0 0 1 159 79Z" class="fd"/>
    <path d="M130 79 L159 79 A29 29 0 0 1 130 108Z" class="fb"/>
    <path d="M130 79 L130 108 A29 29 0 0 1 101 79Z" class="fm"/>
    <path d="M130 79 L101 79 A29 29 0 0 1 130 50Z" class="fl"/>
    <circle cx="130" cy="79" r="20" fill="#f3f7fb" stroke="#d5e2ee" stroke-width=".6"/>
    <text x="118" y="81.5" font-size="7.5" font-weight="800" fill="#1f2a37">SWOT</text>
    <g font-size="3.4" fill="#fff" font-weight="700"><text x="139" y="60">01</text><text x="151" y="95">02</text><text x="115" y="100">03</text><text x="106" y="65">04</text></g>
    <g font-size="4.4" font-weight="700" fill="#0054AA"><text x="24" y="33">STRENGTHS</text><text x="194" y="33">WEAKNESSES</text><text x="24" y="126">OPPORTUNITIES</text><text x="214" y="126">THREATS</text></g>
    <g font-size="2.8" fill="#3a4656">
      <text x="20" y="40">• Mortgage specialization</text><text x="20" y="44.6">• Broad loan program</text><text x="20" y="49.2">• Program management expertise</text><text x="20" y="53.8">• NBFI market share</text><text x="20" y="58.4">• Servicing capabilities</text><text x="20" y="63">• Off balance sheet loan book</text>
      <text x="164" y="40">• Mortgage only</text><text x="164" y="44.6">• Ready-unit only</text><text x="164" y="49.2">• Single program reliance</text><text x="164" y="53.8">• Geographical reach</text><text x="164" y="58.4">• Revenue stream dependency</text><text x="164" y="63">• Small on-balance portfolio</text>
      <text x="20" y="92">• Grow share of existing products</text><text x="20" y="96.6">• Explore new markets</text><text x="20" y="101.2">• Develop new mortgage products</text><text x="20" y="105.8">• Digital innovation</text><text x="20" y="110.4">• Develop new business lines</text>
      <text x="164" y="88">• Subsidy rule shift</text><text x="164" y="92.6">• HSF and ministry shift</text><text x="164" y="97.2">• Speed of digital change</text><text x="164" y="101.8">• Regulatory oversight</text><text x="164" y="106.4">• Pressure from banks</text><text x="164" y="111">• Macro factors (rates, prices)</text>
    </g>
  </svg>
  <div class="foot"><span>12</span><span>© Copyright 2023 Sanad Home Finance. All Rights Reserved.</span></div>
</section>

<section class="slide" style="left:890px;top:526px">
  <div class="title">Competitor Financial Comparison</div>
  <div class="brand"><i></i>Sanad Home Finance</div>
  <svg width="260" height="146" viewBox="0 0 260 146">
    <g font-size="2.5" text-anchor="middle" fill="#fff" font-weight="700">
      <rect x="16" y="27" width="40" height="6" class="fd"/><text x="36" y="31">H1 2023</text>
      <rect x="56" y="27" width="16" height="6" class="fb"/><text x="64" y="31">SHF</text>
      <rect x="72" y="27" width="16" height="6" class="fb"/><text x="80" y="31">Ruwad</text>
      <rect x="88" y="27" width="16" height="6" class="fb"/><text x="96" y="31">Nordfin</text>
      <rect x="104" y="27" width="16" height="6" class="fb"/><text x="112" y="31">Maskan</text>
      <rect x="120" y="27" width="16" height="6" class="fm"/><text x="128" y="31">Dirah</text>
      <rect x="136" y="27" width="16" height="6" class="fm"/><text x="144" y="31">Wadi</text>
      <rect x="152" y="27" width="16" height="6" class="fm"/><text x="160" y="31">Qimma</text>
      <rect x="168" y="27" width="16" height="6" class="fl"/><text x="176" y="31">Fajr</text>
    </g>
    <g fill="#E8F1F8"><rect x="16" y="34" width="168" height="9"/><rect x="16" y="52" width="168" height="9"/><rect x="16" y="70" width="168" height="9"/><rect x="16" y="88" width="168" height="9"/></g>
    <g font-size="2.6" text-anchor="middle" fill="#1f2a37">
      <text x="36" y="39.5">Paid Capital (M)</text><text x="36" y="48.5">Total Assets (M)</text><text x="36" y="57.5">Equity (M)</text><text x="36" y="66.5">Borrowings (M)</text><text x="36" y="75.5">Portfolio Size (M)</text><text x="36" y="84.5">Net Income (M)</text><text x="36" y="93.5">ROE (annualized)</text>
      <text x="64" y="39.5">359</text><text x="80" y="39.5">900</text><text x="96" y="39.5">575</text><text x="112" y="39.5">1,000</text><text x="128" y="39.5">900</text><text x="144" y="39.5">1,000</text><text x="160" y="39.5">714</text><text x="176" y="39.5">300</text>
      <text x="64" y="48.5">969</text><text x="80" y="48.5">3,050</text><text x="96" y="48.5">2,324</text><text x="112" y="48.5">4,307</text><text x="128" y="48.5">3,555</text><text x="144" y="48.5">2,085</text><text x="160" y="48.5">1,521</text><text x="176" y="48.5">889</text>
      <text x="64" y="57.5">589</text><text x="80" y="57.5">892</text><text x="96" y="57.5">700</text><text x="112" y="57.5">1,663</text><text x="128" y="57.5">1,192</text><text x="144" y="57.5">1,342</text><text x="160" y="57.5">882</text><text x="176" y="57.5">366</text>
      <text x="64" y="66.5">36</text><text x="80" y="66.5">1,705</text><text x="96" y="66.5">1,500</text><text x="112" y="66.5">2,544</text><text x="128" y="66.5">2,031</text><text x="144" y="66.5">669</text><text x="160" y="66.5">595</text><text x="176" y="66.5">405</text>
      <text x="64" y="75.5">10,080</text><text x="80" y="75.5">2,855</text><text x="96" y="75.5">2,130</text><text x="112" y="75.5">4,076</text><text x="128" y="75.5">3,246</text><text x="144" y="75.5">1,895</text><text x="160" y="75.5">1,019</text><text x="176" y="75.5">725</text>
      <text x="64" y="84.5">29.2</text><text x="80" y="84.5" fill="#0054AA" font-weight="700">(48.6)</text><text x="96" y="84.5">2.0</text><text x="112" y="84.5">8.6</text><text x="128" y="84.5">34.6</text><text x="144" y="84.5">107.4</text><text x="160" y="84.5">57.0</text><text x="176" y="84.5">55.8</text>
      <text x="64" y="93.5">4.9%</text><text x="80" y="93.5" fill="#0054AA" font-weight="700">(5.4%)</text><text x="96" y="93.5">0.2%</text><text x="112" y="93.5">0.6%</text><text x="128" y="93.5">3.0%</text><text x="144" y="93.5">8.0%</text><text x="160" y="93.5">6.5%</text><text x="176" y="93.5">15%</text>
    </g>
    <path d="M57 99 Q57 103 66 103 L110 103 Q119 103 119 99" fill="none" class="sb" stroke-width=".5"/>
    <path d="M121 99 Q121 103 128 103 L146 103 Q151 103 151 99" fill="none" class="sm" stroke-width=".5"/>
    <path d="M153 99 Q153 103 160 103 L177 103 Q184 103 184 99" fill="none" class="sl" stroke-width=".5"/>
    <rect x="76" y="106" width="26" height="7" class="fb"/><text x="89" y="110.6" font-size="2.8" fill="#fff" text-anchor="middle">Mainly HSF</text>
    <rect x="123" y="106" width="26" height="7" class="fm"/><text x="136" y="110.6" font-size="2.8" fill="#fff" text-anchor="middle">HSF &amp; SME</text>
    <rect x="156" y="106" width="26" height="7" class="fl"/><text x="169" y="110.6" font-size="2.8" fill="#003B7A" text-anchor="middle">PF &amp; SME</text>
  </svg>
  <div class="kh" style="left:191px;top:38px;width:62px;font-size:3.3px"><b class="h">Key Highlights</b><ul><li>HSF peers' net income took a hit in 2023 from high borrowing costs and interest rate mismatch</li><li>Peers active in personal finance and SME lending have the highest ROE</li></ul></div>
  <div class="foot"><span>15</span><span>© Copyright 2023 Sanad Home Finance. All Rights Reserved.</span></div>
</section>

<!-- Row 4 -->
<section class="slide" style="left:51px;top:736px">
  <div class="brand"><i></i>Sanad Home Finance</div>
  <div class="section-line" style="top:43px"></div>
  <div class="section-dot" style="left:116px;top:30px"></div>
  <div class="section-text" style="top:64px">2. Strategy and Financial Plan</div>
  <div class="section-line grey" style="top:96px"></div>
  <div class="foot"><span>16</span><span>© Copyright 2023 Sanad Home Finance. All Rights Reserved.</span></div>
</section>

<section class="slide" style="left:331px;top:736px">
  <div class="brand"><i></i>Sanad Home Finance</div>
  <div class="statement-head">Transformation<br>Strategy<br>Statement</div>
  <div class="statement-body">
    <p>As we transform into a full financial services company, we remain committed to keep extending our range and reach of mortgage solutions.</p>
    <p style="margin-top:4px">Our strategy involves growing our offer beyond mortgages to deliver a broader range of financial solutions to consumers and small and medium firms, while keeping our commitment to tailored service and digital progress.</p>
  </div>
  <div class="statement-art" role="img" aria-label="Photo of a panelled house wall with a front door and two wall lamps"></div>
  <div class="statement-door" role="img" aria-label="Front door of a home"></div>
  <div class="foot"><span>17</span><span>© Copyright 2023 Sanad Home Finance. All Rights Reserved.</span></div>
</section>

<section class="slide" style="left:611px;top:736px">
  <div class="title">Current and Future State Comparison</div>
  <div class="brand"><i></i>Sanad Home Finance</div>
  <div class="col-label" style="left:47px;top:26px;color:var(--blue-mid)">Current State</div>
  <div class="col-label" style="left:140px;top:26px;color:var(--blue)">Future State</div>
  <div class="pill now" style="top:40px">Mortgage originator &amp;<br>service provider</div>
  <div class="pill now" style="top:62px">Single Program Value<br>Proposition</div>
  <div class="pill now" style="top:84px">Limited Geographic<br>Reach</div>
  <div class="pill now" style="top:106px">Single Source of<br>Funding</div>
  <div class="pill next" style="top:36px">Financial Services</div>
  <div class="pill next" style="top:58px">Diverse finance<br>solutions</div>
  <div class="pill next" style="top:80px">Expansive<br>Geographic Reach</div>
  <div class="pill next" style="top:102px">Multiple Sources of<br>Funding</div>
  <div class="foot"><span>18</span><span>© Copyright 2023 Sanad Home Finance. All Rights Reserved.</span></div>
</section>

<section class="slide" style="left:890px;top:736px">
  <div class="title">Financial Objectives and KPIs</div>
  <div class="brand"><i></i>Sanad Home Finance</div>
  <div class="kpi-head" style="left:18px;width:54px;background:var(--blue-mid)">Financial KPIs</div>
  <div class="kpi-head" style="left:129px;width:104px;background:var(--blue)">Production and Customer KPIs</div>
  <div class="kpi-row" style="left:19px;top:48px;font-size:4px"><span style="width:21px"></span><span class="v">2023</span><span class="v">2026</span><span class="v">Change</span></div>
  <div class="kpi-row" style="left:130px;top:48px;font-size:4px"><span style="width:21px"></span><span class="v">2023</span><span class="v">2026</span><span class="v">Change</span></div>
  <div class="kpi-row" style="left:18px;top:60px"><span class="chev" style="width:21px;background:var(--blue-mid)">Portfolio<br>Size</span><span class="v">15.5B</span><span class="v">20.5B</span><span class="chev" style="width:24px;background:var(--blue-light);color:var(--blue-deep)">+ 32%</span></div>
  <div class="kpi-row" style="left:18px;top:76px"><span class="chev" style="width:21px;background:var(--blue-mid)">Net<br>Income</span><span class="v">29.3M</span><span class="v">50.3M</span><span class="chev" style="width:24px;background:var(--blue-light);color:var(--blue-deep)">+ 72%</span></div>
  <div class="kpi-row" style="left:18px;top:92px"><span class="chev" style="width:21px;background:var(--blue-mid)">ROE</span><span class="v">4.9%</span><span class="v">TBD</span><span class="chev" style="width:24px;background:var(--blue-light)"></span></div>
  <div class="kpi-row" style="left:129px;top:60px"><span class="chev" style="width:21px;background:var(--blue)">Market<br>Share</span><span class="v">1.7%</span><span class="v">2.1%</span><span class="chev" style="width:24px;background:var(--blue-pale);color:var(--blue-deep)">+ 24%</span></div>
  <div class="kpi-row" style="left:129px;top:76px"><span class="chev" style="width:21px;background:var(--blue)">HSF Rank</span><span class="v"># 8</span><span class="v"># 7</span><span class="chev" style="width:24px;background:var(--blue-pale);color:var(--blue-deep)">+ 1</span></div>
  <div class="kpi-row" style="left:129px;top:92px"><span class="chev" style="width:21px;background:var(--blue)">Turnaround<br>Time</span><span class="v">21 days</span><span class="v">12 days</span><span class="chev" style="width:24px;background:var(--blue-pale);color:var(--blue-deep)">+ 43%</span></div>
  <div style="position:absolute;left:16px;top:120px;font-size:3.4px;color:var(--text)">* Work in progress. To be finalized prior to Board strategy session.</div>
  <div class="foot"><span>19</span><span>© Copyright 2023 Sanad Home Finance. All Rights Reserved.</span></div>
</section>

<!-- Row 5 -->
<section class="slide" style="left:51px;top:946px">
  <div class="title">5 SHF Transformation Pillars</div>
  <div class="brand"><i></i>Sanad Home Finance</div>
  <svg width="260" height="146" viewBox="0 0 260 146"><path d="M22 50 L130 24 L238 50Z" class="fp" stroke="#7BADD7" stroke-width=".5"/>
    <rect x="22" y="115" width="216" height="8" fill="#5b6b7c"/><text x="130" y="120.5" font-size="3.8" font-weight="700" fill="#fff" text-anchor="middle">SHF Transformation Pillars</text></svg>
  <div class="pillar" style="left:23px;background:var(--blue-deep)">Market<br>Penetration</div>
  <div class="pillar" style="left:66px;background:var(--blue)">Product<br>Development</div>
  <div class="pillar" style="left:109px;background:var(--blue-mid)">Market<br>Development</div>
  <div class="pillar" style="left:152px;background:#3f91c9">Diversification</div>
  <div class="pillar" style="left:195px;background:var(--blue-light)">Technology</div>
  <svg width="260" height="146" viewBox="0 0 260 146" fill="none" stroke="#fff" stroke-width=".7">
    <circle cx="43.5" cy="66" r="4.5"/><path d="M41.5 66 L43 67.5 L46 64.5"/>
    <rect x="82.5" y="62" width="8" height="8" rx="1"/><line x1="86.5" y1="63.5" x2="86.5" y2="68.5"/><line x1="84" y1="66" x2="89" y2="66"/>
    <path d="M125 70 L129.5 62 L134 70Z"/>
    <rect x="168.5" y="61" width="7" height="9"/><line x1="170" y1="64" x2="174" y2="64"/><line x1="170" y1="66.5" x2="174" y2="66.5"/>
    <circle cx="215.5" cy="66" r="4.5"/><circle cx="215.5" cy="66" r="2"/>
  </svg>
  <div class="foot"><span>20</span><span>© Copyright 2023 Sanad Home Finance. All Rights Reserved.</span></div>
</section>

<section class="slide" style="left:331px;top:946px">
  <div class="title">Pillar #1: Market Penetration</div>
  <div class="badge"><b>+200</b>million<br>production<br>impact</div>
  <div class="sub" style="top:28px;right:40px">Grow market share of residential finance in existing market</div>
  <div class="bar" style="left:27px;width:194px;top:37px">Market Penetration</div>
  <div class="card" style="left:27px;top:47px;width:45px;height:83px"><div class="card-head">Improve<br>Productivity</div><ul class="card-body"><li>Raise output across all regions</li><li>Focus on weak and low performers</li><li>Revise the sales incentive plan</li><li>Run seasonal sales drives</li><li>Weekly pipeline reviews</li></ul></div>
  <div class="card" style="left:76px;top:47px;width:45px;height:83px"><div class="card-head">Increase Leads &amp;<br>Conversion</div><ul class="card-body"><li>Revise lead assignment and use criteria</li><li>Keep improving SHF marketing work</li><li>Track conversion by channel</li><li>Faster follow-up on new leads</li></ul></div>
  <div class="card" style="left:125px;top:47px;width:45px;height:83px"><div class="card-head">Increase<br>Sales Head Count</div><ul class="card-body"><li>More sales staff in branches in the three main cities</li><li>New headcount for new branches</li><li>Structured onboarding for new hires</li></ul></div>
  <div class="card" style="left:174px;top:47px;width:47px;height:83px"><div class="card-head">Implement CRM<br>Platform</div><ul class="card-body"><li>Better customer relationships</li><li>Richer data management</li><li>More efficient sales and marketing processes</li><li>Clear view of the full pipeline</li></ul></div>
  <div class="foot"><span>21</span><span>© Copyright 2023 Sanad Home Finance. All Rights Reserved.</span></div>
</section>

<section class="slide" style="left:611px;top:946px">
  <div class="title">Pillar #2: Product Development</div>
  <div class="badge"><b>+500</b>million<br>production<br>impact</div>
  <div class="sub" style="top:26px;right:60px;left:0">Develop new residential finance products for existing market</div>
  <div class="tile" style="left:14px;top:40px;width:110px;height:14px;justify-content:flex-start;padding-left:10px;font-size:4.4px">Residential Finance Products</div>
  <div class="tile" style="left:139px;top:40px;width:112px;height:14px;justify-content:flex-start;padding-left:10px;font-size:4.4px">Partner Programs</div>
  <div class="tile" style="left:14px;top:60px;width:26px;height:36px">Off Plan</div>
  <div class="tile" style="left:42px;top:60px;width:26px;height:36px">Self<br>Construction</div>
  <div class="tile" style="left:70px;top:60px;width:26px;height:36px">Rent<br>-to-<br>Own</div>
  <div class="tile" style="left:98px;top:60px;width:26px;height:36px">Mortgage<br>Savings<br>Program</div>
  <div class="tile" style="left:139px;top:60px;width:27px;height:36px">Manazil<br>Upgrades</div>
  <div class="tile" style="left:168px;top:60px;width:27px;height:36px">HSF<br>New<br>Programs</div>
  <div class="tile" style="left:197px;top:60px;width:26px;height:36px">Partner<br>Upgrades</div>
  <div class="tile" style="left:225px;top:60px;width:26px;height:36px">Banks<br>New<br>Programs</div>
  <div class="tile-note" style="left:14px;top:100px;width:110px">New home finance products that widen the offer beyond ready units and reach first-time buyers earlier in their journey.</div>
  <div class="tile-note" style="left:139px;top:100px;width:112px">Deeper ties with housing programs and banks to grow volume through shared channels and new joint programs.</div>
  <div class="foot"><span>22</span><span>© Copyright 2023 Sanad Home Finance. All Rights Reserved.</span></div>
</section>

<section class="slide" style="left:890px;top:946px">
  <div class="title">Pillar #2: Product Development - Residential</div>
  <div class="brand"><i></i>Sanad Home Finance</div>
  <div class="sub" style="top:25px">Develop new residential finance products for existing market</div>
  <div class="bar" style="left:27px;width:194px;top:34px">Residential Finance Products</div>
  <div class="card" style="left:27px;top:45px;width:45px;height:85px"><div class="card-head" style="padding:5px 1px">Off Plan</div><ul class="card-body"><li>Pending regulator approval</li><li>Build key ties with off-plan developers</li><li>Secure presence at partner centers</li><li>Add new product features</li></ul></div>
  <div class="card" style="left:76px;top:45px;width:45px;height:85px"><div class="card-head" style="padding:5px 1px">Self Construction</div><ul class="card-body"><li>Subject to required approvals</li><li>Develop and launch Self Construction</li><li>Tie up with modern builders</li><li>Include renovation</li></ul></div>
  <div class="card" style="left:125px;top:45px;width:45px;height:85px"><div class="card-head" style="padding:5px 1px">Rent-to-Own</div><ul class="card-body"><li>New concept subject to regulator approval</li><li>Replace down payment with a balloon payment</li><li>Lease-to-own model adapted for housing programs</li></ul></div>
  <div class="card" style="left:174px;top:45px;width:47px;height:85px"><div class="card-head" style="padding:1.8px 1px">Mortgage Savings<br>Program</div><ul class="card-body"><li>New concept subject to regulator approval</li><li>Promotes home ownership and savings</li><li>In line with the national savings plan</li></ul></div>
  <div class="foot"><span>23</span><span>© Copyright 2023 Sanad Home Finance. All Rights Reserved.</span></div>
</section>

</body>
</html>
```